I need a new business card design for my pharmacy.

I need a business card design. I will include my logo.
The card needs to be readable. I prefer to have my logo on one side along with my website, the other side includes the other information. Please use combination of black, neon green, white, and silver. This needs to catch the eye but yet be clearly visible and legible. Thanks

Industry/Entity Type

Pharmacy

Contact Information for Business Card

It needs to have the following information listed:
Mel's Apothecary Owner/Pharm D.
7134 North Brook Lane
Maple Grove, NE 68417
Phone 605-318-6207
Fax 605-318-6209
email: mel@melsapothecary-example.com
www.melsapothecary-example.com
Store hours Monday-Friday 9 am- 6 pm
Saturday 9 am- 1 pm
Sunday Closed
Please utilize the colors black, white, and neon green, maybe silver.

Requirements
Must have
• It needs to be easily readable!
Nice to have
• It should catch the eye.
Should not have
• Do not use any other colors except listed: black, neon green, white, & silver.

```html
<!DOCTYPE html>
<html lang="en">
<head>
<meta charset="utf-8">
<title>Mel's Apothecary – Business Card</title>
<link rel="stylesheet" href="https://fonts.googleapis.com/css2?family=Lato:wght@400;700&family=Arimo:wght@400;700&display=swap">
<style>
  :root {
    --canvas: #ececec;
    --paper: #ffffff;
    --charcoal: #4a4a4a;
    --ink: #3d3d3d;
    --silver: #9a9a9a;
    --neon: #b5d334;
    --white: #ffffff;
  }
  * { box-sizing: border-box; margin: 0; padding: 0; }
  html, body { width: 1200px; height: 1000px; overflow: hidden; }
  body {
    background: var(--canvas);
    position: relative;
    font-family: "Arimo", Arial, sans-serif;
  }
  .card {
    position: absolute;
    top: 357px;
    width: 500px;
    height: 286px;
    border-radius: 2px;
    box-shadow: 0 10px 30px rgba(0,0,0,0.12);
  }
  /* Front */
  .card-front {
    left: 70px;
    background: var(--paper);
    display: flex;
    flex-direction: column;
    align-items: center;
    justify-content: center;
    gap: 26px;
  }
  .brand {
    display: flex;
    align-items: center;
    gap: 16px;
  }
  .brand-dot {
    width: 18px;
    height: 18px;
    border-radius: 50%;
    background: var(--neon);
  }
  .brand-rule {
    width: 1px;
    height: 40px;
    background: var(--ink);
  }
  .brand-name {
    font-family: "Lato", Arial, sans-serif;
    font-weight: 700;
    font-size: 30px;
    color: var(--ink);
    letter-spacing: -0.3px;
  }
  .website {
    font-family: "Lato", Arial, sans-serif;
    font-size: 12px;
    letter-spacing: 4px;
    color: var(--silver);
  }
  /* Back */
  .card-back {
    left: 630px;
    background: var(--charcoal);
    color: var(--white);
    padding: 0 18px;
    text-align: center;
    display: flex;
    flex-direction: column;
    justify-content: center;
  }
  .back-dot {
    width: 18px;
    height: 18px;
    border-radius: 50%;
    border: 2px solid var(--white);
    margin: 0 auto 14px;
  }
  .title {
    font-weight: 700;
    font-size: 17px;
    color: var(--neon);
    margin-bottom: 14px;
  }
  .details {
    display: flex;
    justify-content: center;
    font-size: 13px;
    line-height: 18px;
  }
  .contact {
    font-style: normal;
    text-align: right;
    padding-right: 12px;
    border-right: 1px solid var(--white);
  }
  .hours {
    text-align: left;
    padding-left: 12px;
    padding-top: 18px;
  }
  .hours-title { font-weight: 700; }
  strong { font-weight: 700; }
</style>
</head>
<body>
  <section class="card card-front" aria-label="Business card front">
    <div class="brand">
      <span class="brand-dot"></span>
      <span class="brand-rule"></span>
      <span class="brand-name">Mel's Apothecary</span>
    </div>
    <p class="website">www.melsapothecary-example.com</p>
  </section>

  <section class="card card-back" aria-label="Business card back">
    <div class="back-dot"></div>
    <h1 class="title">Mel's Apothecary Owner/Pharm D.</h1>
    <div class="details">
      <address class="contact">
        7134 North Brook Lane<br>
        Maple Grove, NE 68417<br>
        Phone <strong>605-318-6207</strong><br>
        Fax <strong>605-318-6209</strong><br>
        email: <strong>mel@melsapothecary-example.com</strong>
      </address>
      <div class="hours">
        <div class="hours-title">Store hours</div>
        Monday-Friday 9 am- 6 pm<br>
        Saturday 9 am- 1 pm<br>
        Sunday Closed
      </div>
    </div>
  </section>
</body>
</html>
```